Business Card

Yes I would like you to design me a business card with the logo you just made me

Industry/Entity Type

Business

Colors
33b7a4
00a990
333333
000000
757575
7f7f7f

```html
<!DOCTYPE html>
<html lang="en">
<head>
<meta charset="utf-8">
<title>Mara Velin Photography – Business Card</title>
<link rel="stylesheet" href="https://fonts.googleapis.com/css2?family=Barlow:wght@500&family=Montserrat:wght@700&display=swap">
<style>
  :root {
    --bleed: #d1d3d4;
    --card: #ffffff;
    --blue: #1ca3d9;
    --green: #00a990;
    --ink: #333333;
    --mark: #2b2b2b;
    --crop: #555555;
  }
  html, body {
    margin: 0;
    padding: 0;
    width: 1200px;
    height: 1000px;
    overflow: hidden;
    background: #ffffff;
  }
  .sheet { display: block; width: 1200px; height: 1000px; }
  .bleed-area { fill: var(--bleed); }
  .card-face { fill: var(--card); }
  .card-back { fill: var(--blue); }
  .strip-blue { fill: var(--blue); }
  .strip-green { fill: var(--green); }
  .strip-divider { stroke: #ffffff; stroke-width: 3; }
  .crop-mark { stroke: var(--crop); stroke-width: 1; }
  .icon-ring { fill: none; stroke: #ffffff; stroke-width: 1.6; }
  .icon-line { fill: none; stroke: #ffffff; stroke-width: 1.4; stroke-linecap: round; stroke-linejoin: round; }
  .contact-text {
    font-family: "Barlow", sans-serif;
    font-weight: 500;
    font-size: 17.5px;
    fill: var(--ink);
  }
  .person-name {
    font-family: "Montserrat", sans-serif;
    font-weight: 700;
    font-size: 22px;
    fill: var(--green);
  }
  .person-role {
    font-family: "Barlow", sans-serif;
    font-weight: 500;
    font-size: 16px;
    fill: var(--ink);
  }
  .brand-dot { fill: var(--mark); }
  .brand-name {
    font-family: "Barlow", sans-serif;
    font-weight: 500;
    fill: var(--mark);
  }
  .brand-name--front { font-size: 23px; }
  .brand-name--back { font-size: 28px; }
</style>
</head>
<body>
<svg class="sheet" viewBox="0 0 1200 1000" xmlns="http://www.w3.org/2000/svg">

  <!-- Front side -->
  <g class="card card--front">
    <rect class="bleed-area" x="345" y="32" width="596" height="400"/>
    <rect class="card-face" x="365" y="52" width="556" height="360" rx="18"/>

    <path class="strip-blue" d="M383 52 H398 V268 L365 287 V70 A18 18 0 0 1 383 52 Z"/>
    <path class="strip-green" d="M365 287 L398 268 V412 H383 A18 18 0 0 1 365 394 Z"/>
    <line class="strip-divider" x1="365" y1="286" x2="398" y2="267"/>

    <g class="crop-marks">
      <line class="crop-mark" x1="365" y1="8" x2="365" y2="52"/>
      <line class="crop-mark" x1="921" y1="8" x2="921" y2="52"/>
      <line class="crop-mark" x1="316" y1="52" x2="365" y2="52"/>
      <line class="crop-mark" x1="921" y1="52" x2="971" y2="52"/>
      <line class="crop-mark" x1="365" y1="412" x2="365" y2="472"/>
      <line class="crop-mark" x1="921" y1="412" x2="921" y2="472"/>
      <line class="crop-mark" x1="316" y1="412" x2="365" y2="412"/>
      <line class="crop-mark" x1="921" y1="412" x2="971" y2="412"/>
    </g>

    <g class="contact-icons">
      <circle class="icon-ring" cx="381" cy="108" r="10"/>
      <path class="icon-line" d="M377 103 q-1 4 2 8 q3 3 7 2 l1 -2 -3 -2 -1 1 q-3 -1 -4 -4 l1 -1 -2 -3 z"/>
      <circle class="icon-ring" cx="381" cy="137" r="10"/>
      <rect class="icon-line" x="375" y="132.5" width="12" height="9"/>
      <path class="icon-line" d="M375 133 L381 138 L387 133"/>
      <circle class="icon-ring" cx="381" cy="166" r="10"/>
      <circle class="icon-line" cx="381" cy="166" r="6.5"/>
      <ellipse class="icon-line" cx="381" cy="166" rx="3" ry="6.5"/>
      <line class="icon-line" x1="374.5" y1="166" x2="387.5" y2="166"/>
      <circle class="icon-ring" cx="381" cy="195" r="10"/>
    </g>

    <g class="contact-list">
      <text class="contact-text" x="408" y="114">555-210-4836</text>
      <text class="contact-text" x="408" y="143">hello@maravelinphoto.com</text>
      <text class="contact-text" x="410" y="172">www.maravelinphoto.com</text>
      <text class="contact-text" x="406" y="201">@maravelinphotography</text>
    </g>

    <g class="person">
      <text class="person-name" x="500" y="330" text-anchor="middle">Mara Velin</text>
      <text class="person-role" x="500" y="348" text-anchor="middle">Photographer</text>
    </g>

    <g class="brand brand--front">
      <circle class="brand-dot" cx="764" cy="270" r="28"/>
      <text class="brand-name brand-name--front" x="774" y="334" text-anchor="middle">mara velin photography</text>
    </g>
  </g>

  <!-- Back side -->
  <g class="card card--back">
    <rect class="bleed-area" x="345" y="556" width="596" height="400"/>
    <rect class="card-back" x="365" y="576" width="556" height="360" rx="18"/>

    <g class="crop-marks">
      <line class="crop-mark" x1="365" y1="532" x2="365" y2="576"/>
      <line class="crop-mark" x1="921" y1="532" x2="921" y2="576"/>
      <line class="crop-mark" x1="317" y1="576" x2="365" y2="576"/>
      <line class="crop-mark" x1="921" y1="576" x2="971" y2="576"/>
      <line class="crop-mark" x1="365" y1="936" x2="365" y2="996"/>
      <line class="crop-mark" x1="921" y1="936" x2="921" y2="996"/>
      <line class="crop-mark" x1="317" y1="936" x2="365" y2="936"/>
      <line class="crop-mark" x1="921" y1="936" x2="971" y2="936"/>
    </g>

    <g class="brand brand--back">
      <circle class="brand-dot" cx="636" cy="722" r="33"/>
      <text class="brand-name brand-name--back" x="650" y="808" text-anchor="middle">mara velin photography</text>
    </g>
  </g>

</svg>
</body>
</html>
```